Bramblenest.com Greeting cards

We need a total of 15 digital greeting cards. in the following categories of life milestones. 3 of each to start.

1. Bar Mitzvah and Bat Mitzvah
2. Sweet 16
3. Babies Birth
4. Anniversary
5. Birthday

```html
<!DOCTYPE html>
<html lang="en">
<head>
<meta charset="utf-8">
<title>Happy Birthday Card</title>
<link rel="stylesheet" href="https://fonts.googleapis.com/css2?family=Varela+Round&display=swap">
<style>
  :root {
    --backdrop: #3a2a1f;
    --card-navy: #1c2a4f;
    --orange: #f7a23b;
    --pink: #ee4f9e;
    --green: #a8d24a;
    --teal: #4fc3c8;
    --kid-green: #5aa83d;
    --kid-yellow: #f4c870;
    --kid-blue: #8fb8e8;
  }
  html, body {
    margin: 0;
    width: 1200px;
    height: 900px;
    overflow: hidden;
    background: var(--backdrop);
  }
  .birthday-card {
    position: absolute;
    left: 80px;
    top: 48px;
    width: 1040px;
    height: 805px;
    display: block;
  }
  .card-face { fill: var(--card-navy); }
  .ground-band { fill: var(--green); }
  .greeting {
    font-family: "Varela Round", "Nunito", sans-serif;
    font-weight: 700;
    text-anchor: middle;
    letter-spacing: 2px;
  }
  .greeting-happy { fill: var(--orange); font-size: 112px; }
  .greeting-birthday { fill: var(--pink); font-size: 112px; }
  .flag-orange, .star-orange { fill: var(--orange); }
  .flag-pink, .star-pink { fill: var(--pink); }
  .flag-green, .star-green { fill: var(--green); }
  .flag-teal { fill: var(--teal); }
  .kid-spot { opacity: 0.85; }
  .kid-girl-green { fill: var(--kid-green); }
  .kid-boy-yellow { fill: var(--kid-yellow); }
  .kid-girl-blue { fill: var(--kid-blue); }
</style>
</head>
<body>
<svg class="birthday-card" viewBox="180 125 840 650" xmlns="http://www.w3.org/2000/svg">
  <defs>
    <path id="star" d="M0,-16 L4.7,-5.2 L15.2,-4.9 L7.6,2.6 L9.4,13 L0,8 L-9.4,13 L-7.6,2.6 L-15.2,-4.9 L-4.7,-5.2 Z"/>
  </defs>

  <rect class="card-face" x="180" y="125" width="840" height="650"/>

  <g class="bunting bunting-left">
    <polygon class="flag-orange" points="180,125 222,150 188,178"/>
    <polygon class="flag-green" points="222,150 270,178 238,208"/>
    <polygon class="flag-teal" points="270,178 325,198 292,240"/>
    <polygon class="flag-pink" points="325,198 383,208 352,258"/>
    <polygon class="flag-orange" points="383,208 442,205 412,265"/>
    <polygon class="flag-green" points="442,205 500,190 462,252"/>
    <polygon class="flag-pink" points="500,190 555,172 540,232"/>
  </g>
  <g class="bunting bunting-top">
    <polygon class="flag-orange" points="528,128 582,148 545,186"/>
    <polygon class="flag-green" points="610,140 662,125 632,172"/>
  </g>
  <g class="bunting bunting-right">
    <polygon class="flag-green" points="578,160 625,185 590,212"/>
    <polygon class="flag-teal" points="625,185 682,200 652,246"/>
    <polygon class="flag-pink" points="682,200 740,210 705,268"/>
    <polygon class="flag-orange" points="740,210 800,210 770,272"/>
    <polygon class="flag-green" points="800,210 858,195 830,262"/>
    <polygon class="flag-pink" points="858,195 915,175 900,240"/>
    <polygon class="flag-teal" points="915,175 970,150 962,210"/>
    <polygon class="flag-green" points="970,150 1020,125 1015,182"/>
  </g>

  <g class="stars">
    <use href="#star" class="star-pink" x="406" y="176"/>
    <use href="#star" class="star-orange" x="237" y="255"/>
    <use href="#star" class="star-pink" x="814" y="165"/>
    <use href="#star" class="star-orange" x="902" y="353"/>
    <use href="#star" class="star-green" x="265" y="425"/>
    <use href="#star" class="star-green" x="487" y="538"/>
    <use href="#star" class="star-pink" x="966" y="521"/>
    <use href="#star" class="star-green" x="230" y="600"/>
    <use href="#star" class="star-green" x="738" y="582"/>
    <use href="#star" class="star-pink" x="470" y="684"/>
    <use href="#star" class="star-pink" x="970" y="683"/>
  </g>

  <text class="greeting greeting-happy" x="602" y="390">HAPPY</text>
  <text class="greeting greeting-birthday" x="605" y="502">BIRTHDAY</text>

  <g class="kids">
    <g role="img" aria-label="Illustration of a smiling girl in a green dress dancing">
      <rect class="kid-spot kid-girl-green" x="272" y="565" width="132" height="195" rx="40"/>
    </g>
    <g role="img" aria-label="Illustration of a cheerful boy in a yellow shirt jumping with arms spread">
      <rect class="kid-spot kid-boy-yellow" x="525" y="575" width="170" height="182" rx="40"/>
    </g>
    <g role="img" aria-label="Illustration of a purple-haired girl in a blue top skipping">
      <rect class="kid-spot kid-girl-blue" x="815" y="560" width="132" height="195" rx="40"/>
    </g>
  </g>

  <rect class="ground-band" x="180" y="757" width="840" height="18"/>
</svg>
</body>
</html>
```